Geschäftspapiere Campingplatz
Zielgruppe
Campingplatz
Aufgabenstellung
Geschäftspapiere, Briefpapier, Visitenkarte, Briefumschlag und DIN A5 Memoblock farblich und designmäßig am Logo orientiert.
Memoblock sollte sich vom Briefpapier unterscheiden und nicht so viele Daten enthalten.
Website, E-Mail, Telefonnummer, Festnetz, Adresse und Inhaber sollen auf dem Briefpapier erscheinen.
Auf der Visitenkarte soll nur statt Inhaber stehen und zusätzlich die Handynummer, sowie alle anderen Daten.
Die Datensätze sollten sich mit entsprechendem Programm von uns bearbeiten lassen.

```html
<!DOCTYPE html>
<html lang="de">
<head>
<meta charset="utf-8">
<title>Camping Wiesengrund – Geschäftsausstattung</title>
<link rel="stylesheet" href="https://fonts.googleapis.com/css2?family=Source+Sans+3:wght@400;600&display=swap">
<style>
:root{
  --bg:#f7f7f7;
  --paper:#ffffff;
  --green:#6e962a;
  --green-band:#7d974e;
  --olive:#ad9a2e;
  --ink:#3a3a3a;
  --grey:#666666;
  --orange:#e8842c;
  --env:#f1f1f1;
  --env-window:#e3e3e3;
  --env-line:#8a8a8a;
  --shadow:3px 4px 6px rgba(0,0,0,.35);
}
*{margin:0;padding:0;box-sizing:border-box}
html,body{width:1200px;height:1000px;overflow:hidden;background:var(--bg)}
body{position:relative;font-family:"Source Sans 3",sans-serif;color:var(--ink)}
.abs{position:absolute}
.brand{font-weight:600;color:var(--green);white-space:nowrap;letter-spacing:.01em}

/* main brand */
.brand-main{left:84px;top:120px;font-size:44px;line-height:1}

/* letterhead */
.letterhead{left:36px;top:213px;width:534px;height:753px;background:var(--paper);box-shadow:var(--shadow)}
.letterhead .bar-olive{left:0;top:0;width:9px;height:124px;background:var(--olive)}
.letterhead .bar-green{left:0;top:132px;width:9px;height:621px;background:var(--green)}
.letterhead .fold{left:9px;width:16px;height:1px;background:var(--grey)}
.letterhead .brand-head{right:31px;top:68px;font-size:18px;line-height:1}
.sender{left:67px;top:139px;font-size:6.5px;color:var(--grey);display:flex;align-items:center;gap:6px}
.sender i{display:inline-block;width:7px;height:7px;border-radius:50%;background:var(--green)}
.contact{left:379px;top:113px;border-left:1.5px solid var(--olive);padding-left:6px;height:135px;font-size:8.3px;line-height:10px}
.contact .name{font-weight:600;color:var(--green);font-size:10px;line-height:12px}
.contact .lbl{color:var(--orange)}
.contact p{margin:0}
.contact .gap{height:19px}
.contact .sp{height:6px}
.footer{top:716px;font-size:7.6px;line-height:8.6px;color:var(--grey)}
.footer-div{top:716px;width:1px;height:23px;background:var(--grey)}

/* business card front */
.card{background:var(--paper);box-shadow:var(--shadow)}
.card-front{left:696px;top:40px;width:345px;height:225px;overflow:hidden}
.card-front .brand-card{left:15px;top:39px;font-size:13.5px;line-height:1}
.card-front .bar-top{left:162px;top:46px;width:183px;height:8px;background:var(--olive)}
.card-front .band{left:0;top:78px;width:345px;height:91px;background:var(--green-band);color:#e8edd9;font-size:7.3px;line-height:9.5px;text-align:center}
.band .item{position:absolute;display:flex;flex-direction:column;align-items:center;gap:2px}
.band svg{width:19px;height:19px}
.card-front .bar-bottom{left:0;top:191px;width:214px;height:9px;background:var(--olive)}
.card-front .holder{left:244px;top:185px;font-size:15px;color:var(--grey)}

/* business card back */
.card-back{left:702px;top:297px;width:344px;height:224px}
.card-back .brand-big{left:0;width:344px;top:94px;text-align:center;font-size:24px}

/* envelope */
.envelope{left:633px;top:537px;width:498px;height:429px}
.env-flap{left:0;top:0;width:498px;height:76px}
.env-body{left:0;top:76px;width:498px;height:353px;background:var(--env);border-top:1px solid var(--env-line);box-shadow:var(--shadow)}
.env-format{left:358px;top:14px;font-size:34px;color:var(--grey);line-height:1}
.env-window{left:45px;top:83px;width:195px;height:75px;border-radius:9px;background:var(--env-window)}
.env-rule{left:0;top:294px;width:317px;height:1px;background:var(--env-line)}
.env-brand{left:334px;top:283px;font-size:13.5px;line-height:1}
.env-address{left:40px;top:312px;width:108px;font-size:8.7px;line-height:11px;text-align:center;color:var(--grey)}
</style>
</head>
<body>

<div class="abs brand brand-main">Camping Wiesengrund</div>

<section class="abs letterhead" aria-label="Briefpapier">
  <div class="abs bar-olive"></div>
  <div class="abs bar-green"></div>
  <div class="abs fold" style="top:265px"></div>
  <div class="abs fold" style="top:518px"></div>

  <div class="abs brand brand-head">Camping Wiesengrund</div>

  <div class="abs sender"><i></i><span>Lindenweg 12&nbsp;&nbsp;&nbsp;&nbsp;74100 Talheim am Fluss</span></div>

  <div class="abs contact">
    <p class="name">Camping Wiesengrund</p>
    <p>Marlene Ostrau</p>
    <div class="gap"></div>
    <p>Address here, number</p>
    <p>City, Country</p>
    <div class="sp"></div>
    <p><span class="lbl">Telefon:</span>&nbsp; 55 555-555-555</p>
    <div class="sp" style="height:2px"></div>
    <p class="lbl">Mobile:</p>
    <p>Marlene 55 555-555-555</p>
    <p>Tobias 55 555-555-555</p>
    <div class="sp" style="height:2px"></div>
    <p><span class="lbl">E-mail:</span>&nbsp;&nbsp; email@yourdomain.com</p>
    <div class="sp" style="height:2px"></div>
    <p><span class="lbl">Web:</span>&nbsp;&nbsp;&nbsp;&nbsp;&nbsp;&nbsp; www.yourwebsite.com</p>
  </div>

  <div class="abs footer" style="left:79px">Bankverbindung<br>Regionalbank Talgrund eG<br>Konto 000000000r</div>
  <div class="abs footer-div" style="left:215px"></div>
  <div class="abs footer" style="left:238px">BLZ: 0000y760000<br>Steurnummer: 000/870000<br>Ust-ID: DE 00008900000</div>
  <div class="abs footer-div" style="left:357px"></div>
  <div class="abs footer" style="left:381px;top:720px">BIC: ETFUuhYGYGU<br>IBAN: 700007900000</div>
</section>

<section class="abs card card-front" aria-label="Visitenkarte Vorderseite">
  <div class="abs brand brand-card">Camping Wiesengrund</div>
  <div class="abs bar-top"></div>
  <div class="abs band">
    <div class="item" style="left:12px;top:26px;width:76px">
      <svg viewBox="0 0 20 20" fill="none" stroke="#e8edd9" stroke-width="1.2"><circle cx="10" cy="10" r="9"/><path d="M5 10.5 10 5.5l5 5M7 9.5V14h6V9.5"/></svg>
      <span>Address here, number<br>City, Country</span>
    </div>
    <div class="item" style="left:120px;top:6px;width:104px">
      <svg viewBox="0 0 20 20" fill="none" stroke="#e8edd9" stroke-width="1.2"><circle cx="10" cy="10" r="9"/><path d="M12.5 5.5c-2 0-5 4.5-4.5 8 .3.8 1.4.9 2 .3M12.5 5.5l.5 2.3M10 14.1l-.2-2"/></svg>
      <span>55 555-555-555</span>
    </div>
    <div class="item" style="left:120px;top:44px;width:104px">
      <svg viewBox="0 0 20 20" fill="none" stroke="#e8edd9" stroke-width="1.2"><circle cx="10" cy="10" r="9"/><rect x="7.5" y="5" width="5" height="10" rx="1"/></svg>
      <span>Tobias 55 555-555-555<br>Marlene 55 555-555-555</span>
    </div>
    <div class="item" style="left:245px;top:6px;width:90px">
      <svg viewBox="0 0 20 20" fill="none" stroke="#e8edd9" stroke-width="1.2"><circle cx="10" cy="10" r="9"/><rect x="5.5" y="7" width="9" height="6.5"/><path d="M5.5 7 10 10.5 14.5 7"/></svg>
      <span>email@yourdomain.com</span>
    </div>
    <div class="item" style="left:245px;top:54px;width:90px">
      <svg viewBox="0 0 20 20" fill="none" stroke="#e8edd9" stroke-width="1.2"><circle cx="10" cy="10" r="9"/><circle cx="10" cy="10" r="5"/><path d="M5 10h10M10 5v10M7.5 5.8c-1.5 2.6-1.5 5.8 0 8.4M12.5 5.8c1.5 2.6 1.5 5.8 0 8.4"/></svg>
      <span>www.yourwebsite.com</span>
    </div>
  </div>
  <div class="abs bar-bottom"></div>
  <div class="abs holder">Fam. Ostrau</div>
</section>

<section class="abs card card-back" aria-label="Visitenkarte Rückseite">
  <div class="abs brand brand-big">Camping Wiesengrund</div>
</section>

<section class="abs envelope" aria-label="Briefumschlag">
  <svg class="abs env-flap" viewBox="0 0 498 76" aria-hidden="true">
    <path d="M2 76 C10 50 20 24 38 8 Q45 1 60 0 H438 Q455 1 464 12 L498 76 Z" fill="#f3f3f3"/>
  </svg>
  <div class="abs env-body">
    <div class="abs env-format">Din A5</div>
    <div class="abs env-window"></div>
    <div class="abs env-rule"></div>
    <div class="abs brand env-brand">Camping Wiesengrund</div>
    <div class="abs env-address">Address here, number<br>City, Country</div>
  </div>
</section>

</body>
</html>
```